Brightwave Reach - Business Card

We need a business card for a Social Media Marketing company that specializes in online marketing for small businesses in Canada using common Social Media platforms such as Pictora, Kinloop, Blinkit & Chirpo.

I have uploaded a copy of our logo which I would like utilized in the business card. We would like the business card to be modern yet classy design.

Our website is www.brightwavereach.ca

Industry/Entity Type

Marketing

Contact Information for Business Card

Email: info@brightwavereach.ca
Website: www.brightwavereach.ca
Telephone: 604-392-5108

Colors

Designer to choose colors to be used in the design.

Requirements
Must have
• Social Media icons on reverse
• Please add some designs with color.

```html
<!DOCTYPE html>
<html lang="en">
<head>
<meta charset="utf-8">
<title>Brightwave Reach – Business Card</title>
<link rel="stylesheet" href="https://fonts.googleapis.com/css2?family=Roboto+Condensed:wght@700&family=Roboto:wght@400;500&display=swap">
<style>
  :root {
    --backdrop: #262728;
    --card-dark: #3a3f42;
    --card-light: #5c6367;
    --ink: #ffffff;
    --ink-soft: #e4e7e8;
  }
  * { margin: 0; padding: 0; box-sizing: border-box; }
  html, body {
    width: 1200px; height: 900px; overflow: hidden;
    background: var(--backdrop);
  }
  .canvas {
    width: 1200px; height: 900px;
    display: flex; flex-direction: column; align-items: center; justify-content: center;
    gap: 40px;
  }
  .card {
    width: 630px; height: 360px;
    background: linear-gradient(120deg, var(--card-dark) 0%, var(--card-light) 100%);
    color: var(--ink);
    position: relative;
  }
  /* Front */
  .card--front {
    display: flex; flex-direction: column; align-items: center; justify-content: center;
    gap: 44px;
  }
  .brand {
    display: flex; align-items: center; gap: 12px;
  }
  .brand__mark {
    width: 22px; height: 22px; border: 3px solid var(--ink);
  }
  .brand__name {
    font-family: "Roboto Condensed", "Arial Narrow", sans-serif;
    font-weight: 700; font-size: 40px; letter-spacing: 1px;
    text-transform: uppercase; color: var(--ink);
  }
  .socials {
    display: flex; gap: 22px; list-style: none;
    font-family: "Roboto", Arial, sans-serif; font-size: 13px; color: var(--ink-soft);
  }
  .socials li { display: flex; align-items: center; gap: 6px; }
  .socials .dot {
    width: 14px; height: 14px; border: 1.5px solid var(--ink); border-radius: 50%;
  }
  /* Back */
  .card--back {
    display: flex; align-items: center; justify-content: center;
  }
  .person {
    text-align: right; padding-right: 26px;
  }
  .person__name {
    font-family: "Roboto Condensed", "Arial Narrow", sans-serif;
    font-weight: 700; font-size: 34px; text-transform: uppercase; line-height: 1;
  }
  .person__role {
    font-family: "Roboto", Arial, sans-serif;
    font-size: 15px; text-transform: uppercase; margin-top: 6px; color: var(--ink-soft);
  }
  .divider {
    width: 2px; height: 100px; background: var(--ink);
  }
  .contacts {
    list-style: none; padding-left: 22px;
    font-family: "Roboto", Arial, sans-serif; font-weight: 500; font-size: 16px;
  }
  .contacts li { display: flex; align-items: center; gap: 10px; line-height: 24px; }
  .contacts svg { width: 14px; height: 14px; fill: var(--ink); flex: none; }
</style>
</head>
<body>
<main class="canvas">
  <section class="card card--front" aria-label="Card front">
    <div class="brand">
      <span class="brand__mark"></span>
      <span class="brand__name">Brightwave Reach</span>
    </div>
    <ul class="socials">
      <li><span class="dot"></span>Kinloop</li>
      <li><span class="dot"></span>Pictora</li>
      <li><span class="dot"></span>Chirpo</li>
    </ul>
  </section>

  <section class="card card--back" aria-label="Card back">
    <div class="person">
      <p class="person__name">Daniel Hart</p>
      <p class="person__role">CEO/Founder</p>
    </div>
    <span class="divider"></span>
    <ul class="contacts">
      <li>
        <svg viewBox="0 0 24 24" aria-hidden="true"><path d="M6.6 10.8a15.1 15.1 0 0 0 6.6 6.6l2.2-2.2a1 1 0 0 1 1-.25 11.4 11.4 0 0 0 3.6.57 1 1 0 0 1 1 1V20a1 1 0 0 1-1 1A17 17 0 0 1 3 4a1 1 0 0 1 1-1h3.5a1 1 0 0 1 1 1c0 1.25.2 2.45.57 3.57a1 1 0 0 1-.25 1z"/></svg>
        604-392-5108
      </li>
      <li>
        <svg viewBox="0 0 24 24" aria-hidden="true"><path d="M2 5h20v14H2z M3 6l9 7 9-7" fill="none" stroke="#fff" stroke-width="2"/></svg>
        info@brightwavereach.ca
      </li>
      <li>
        <svg viewBox="0 0 24 24" aria-hidden="true"><circle cx="12" cy="12" r="9" fill="none" stroke="#fff" stroke-width="2"/><path d="M3 12h18M12 3c3 3 3 15 0 18M12 3c-3 3-3 15 0 18" fill="none" stroke="#fff" stroke-width="1.6"/></svg>
        www.brightwavereach.ca
      </li>
    </ul>
  </section>
</main>
</body>
</html>
```